Website redesign

We need a bold revamp of our website (http://www.brantwoodpower.co.nz/)
which at the moment looks dated. We want a crisp, fresh and bold look. The background image behind web page can go. Open to complete new layout

Target Market(s)

Electrical contracting company- working in the domestic and commercial field

Coding

Coded - Design and coding required

Number of Pages Required

5+ page

Font styles to use
Sans Serif

Colors

Designer to choose colors to be used in the design.

```html
<!DOCTYPE html>
<html lang="en">
<head>
<meta charset="utf-8">
<title>Kowhai Group</title>
<link rel="stylesheet" href="https://fonts.googleapis.com/css2?family=Questrial&family=Open+Sans:wght@400;600&display=swap">
<style>
:root{
  --green:#58ab2c;
  --ink:#222;
  --grey-text:#555;
  --band:#ebebeb;
  --bar:#a6a6a6;
  --footer:#3a3a3a;
  --white:#fff;
  --hero-dark:#050b14;
  --hero-blue:#0f2a48;
  --photo-brick:#8c7b70;
  --photo-grey:#98a0a6;
  --photo-shop:#8f8a86;
}
*{box-sizing:border-box;margin:0;padding:0}
html,body{width:1200px;height:3273px;overflow:hidden}
body{position:relative;font-family:"Open Sans",sans-serif;color:var(--ink);background:var(--white)}
.abs{position:absolute}

/* header */
.site-header{position:absolute;left:0;top:0;width:1200px;height:122px;background:var(--white);z-index:3}
.brand-badge{position:absolute;left:98px;top:-34px;width:230px;height:230px;border-radius:50%;background:var(--white);z-index:4;display:flex;flex-direction:column;align-items:center;justify-content:center;padding-top:40px}
.brand-dot{width:34px;height:34px;border-radius:50%;background:var(--green);margin-bottom:10px}
.brand-name{font-family:"Questrial",sans-serif;color:var(--green);font-size:30px;line-height:1.05;text-align:center}
.main-nav{position:absolute;left:397px;top:48px;display:flex;gap:36px;font-size:16px}
.main-nav a{color:var(--ink);text-decoration:none}
.main-nav a.active{color:var(--green)}
.header-contact{position:absolute;top:36px;display:flex;gap:10px;font-size:15px;line-height:1.3;color:var(--ink)}
.header-contact .label{color:var(--green)}
.divider-v{position:absolute;left:684px;top:34px;width:1px;height:56px;background:#ddd}

/* hero */
.hero{position:absolute;left:0;top:122px;width:1200px;height:515px;background:linear-gradient(100deg,var(--hero-dark) 0%,var(--hero-dark) 40%,var(--hero-blue) 100%)}
.hero-visual{position:absolute;right:0;top:0;width:460px;height:515px;background:linear-gradient(90deg,rgba(15,42,72,0) 0%,#1c3d60 100%)}
.hero h1{position:absolute;left:98px;top:135px;font-family:"Questrial",sans-serif;font-weight:400;font-size:62px;color:var(--white)}
.hero p{position:absolute;left:98px;top:240px;width:470px;font-size:13.5px;line-height:1.75;color:var(--white)}
.btn-outline{position:absolute;left:98px;top:325px;width:109px;height:48px;border:2px solid var(--white);border-radius:4px;color:var(--white);font-size:14px;display:flex;align-items:center;justify-content:center}
.slider-dots{position:absolute;display:flex;gap:5px}
.slider-dots span{width:14px;height:14px;border-radius:2px;background:#555}
.slider-dots span.on{background:var(--white)}

/* section heading */
.section-title{position:absolute;left:0;width:1200px;text-align:center}
.section-title .mark{width:34px;height:34px;border:4px solid var(--green);border-radius:50%;margin:0 auto 22px}
.section-title h2{font-family:"Questrial",sans-serif;font-weight:400;font-size:38px;color:var(--ink)}
.section-title h2 em{font-style:normal;color:var(--green)}
.section-title .rule{width:126px;height:2px;background:var(--green);margin:14px auto 0}

/* about */
.about-text{position:absolute;left:100px;top:856px;width:1000px;text-align:center;font-size:14px;line-height:1.7;color:var(--grey-text)}
.about-text p+p{margin-top:10px}
.btn-green{position:absolute;background:var(--green);color:var(--white);border-radius:3px;font-size:14px;display:flex;align-items:center;justify-content:center}

/* services */
.services{position:absolute;left:0;top:1143px;width:1200px;height:701px;background:var(--band)}
.service-bar{position:absolute;width:415px;height:96px;background:var(--bar);color:var(--white);border-top:4px solid #cfcfcf;border-bottom:3px solid #8f8f8f}
.service-bar.left{left:0;border-radius:0 48px 48px 0;text-align:right;padding-right:120px}
.service-bar.right{left:785px;border-radius:48px 0 0 48px;padding-left:120px}
.service-bar h3{font-family:"Questrial",sans-serif;font-weight:400;font-size:24px;margin-top:16px}
.service-bar small{font-size:14px;display:block;margin-top:2px}
.service-icon{position:absolute;top:4px;width:88px;height:88px;border-radius:50%;background:var(--white);border:4px solid #ddd;display:flex;align-items:center;justify-content:center}
.service-bar.left .service-icon{right:4px}
.service-bar.right .service-icon{left:4px}
.service-icon .disc{width:68px;height:68px;border-radius:50%;background:var(--green);display:flex;align-items:center;justify-content:center}
.service-icon.light .disc{background:var(--white);border:2px solid #eee}
.hub{position:absolute;left:436px;top:1387px;width:328px;height:328px;border-radius:50%;background:var(--white);border:10px solid var(--green);box-shadow:0 0 0 12px #fff;display:flex;flex-direction:column;align-items:center;justify-content:center}
.hub .brand-dot{width:60px;height:60px}
.hub .brand-name{font-size:40px}

/* projects */
.project-photo{position:absolute}
.project-photo.side{border:3px solid #ddd}
.project-photo.main{border:4px solid var(--white);box-shadow:0 0 0 1px #ccc;z-index:2}
.project-caption{position:absolute;left:0;width:1200px;text-align:center}
.project-caption h3{font-family:"Questrial",sans-serif;font-weight:400;font-size:28px;color:var(--green)}
.project-caption p{font-size:14px;color:var(--grey-text);margin-top:8px}

/* footer */
.site-footer{position:absolute;left:0;top:2636px;width:1200px;height:637px;background:var(--footer);color:var(--white)}
.footer-brand{position:absolute;left:98px;top:88px;width:130px;text-align:center}
.footer-brand .brand-name{color:var(--white)}
.footer-brand .brand-dot{margin:0 auto 10px}
.contact-list{position:absolute;left:98px;list-style:none;font-size:18px}
.contact-list li{position:absolute;left:0;display:flex;align-items:center;gap:18px;white-space:nowrap;line-height:1.3}
.contact-list .ico{width:42px;height:36px;border:2px solid var(--white);border-radius:3px;display:flex;align-items:center;justify-content:center;flex:none}
.contact-form{position:absolute;left:556px;top:70px;width:560px}
.contact-form h3{font-family:"Questrial",sans-serif;font-weight:400;font-size:30px}
.contact-form .rule{width:100px;height:2px;background:var(--white);margin-top:8px}
.contact-form .note{font-size:16px;margin-top:26px}
.field-label{position:absolute;left:0;font-size:17px}
.field{position:absolute;left:99px;width:445px;height:37px;border:1.5px solid var(--white);border-radius:3px}
.site-footer .hr{position:absolute;left:98px;top:550px;width:1004px;height:1px;background:#666}
.copyright{position:absolute;left:0;top:584px;width:1200px;text-align:center;font-size:14px}
.version{position:absolute;left:1130px;top:584px;font-size:14px}
</style>
</head>
<body>

<header class="site-header">
  <div class="brand-badge"><div class="brand-dot"></div><div class="brand-name">Kowhai<br>Group</div></div>
  <nav class="main-nav"><a class="active" href="#">Home</a><a href="#">About Us</a><a href="#">Contact Us</a></nav>
  <div class="divider-v"></div>
  <div class="header-contact" style="left:700px">
    <svg width="34" height="26" viewBox="0 0 34 26"><rect x="2" y="2" width="30" height="22" fill="none" stroke="#58ab2c" stroke-width="3"/><path d="M2 2l15 12 15-12" fill="none" stroke="#58ab2c" stroke-width="3"/></svg>
    <div><span class="label">Mail:</span><br>office@kowhaigroup.co.nz</div>
  </div>
  <div class="header-contact" style="left:968px">
    <svg width="22" height="36" viewBox="0 0 22 36"><rect x="2" y="2" width="18" height="32" rx="3" fill="none" stroke="#58ab2c" stroke-width="3"/><circle cx="11" cy="28" r="2" fill="#58ab2c"/></svg>
    <div><span class="label">0800 55 01 20,</span><br>(06) 555 0142</div>
  </div>
</header>

<section class="hero">
  <div class="hero-visual" role="img" aria-label="Photo of a lit light bulb held above an open hand"></div>
  <h1>Kowhai Group</h1>
  <p>Kowhai Electrical is a leading electrical installation and maintenance company based in Wanganui, but servicing all New Zealand.</p>
  <div class="btn-outline">Read More</div>
  <div class="slider-dots" style="left:98px;top:403px"><span class="on"></span><span></span><span></span><span></span><span></span></div>
</section>

<section>
  <div class="section-title" style="top:692px"><div class="mark"></div><h2>About <em>Kowhai Group</em></h2><div class="rule"></div></div>
  <div class="about-text">
    <p>Kowhai Group is a leading electrical installation and maintenance company based in Wanganui, but servicing all New Zealand.<br>With over 15 professionally qualified and experienced Wanganui electricians, technicians and support staff we are leading the way in providing quality electrical services.</p>
    <p>Kowhai Group was established in 1991 and does it all, from supplying and changing light bulbs, comprehensive whole house electrical design and installation, to commercial and large scale industrial consultation, implementation and servicing.</p>
  </div>
  <div class="btn-green" style="left:545px;top:1021px;width:110px;height:48px">Read More</div>
</section>

<section class="services">
  <div class="section-title" style="top:56px"><div class="mark"></div><h2>Our <em>Services</em></h2><div class="rule"></div></div>
</section>
<svg class="abs" style="left:0;top:1346px" width="1200" height="410" viewBox="0 0 1200 410"><path d="M410 40 Q460 60 470 130 M410 365 Q460 345 470 280 M790 40 Q740 60 730 130 M790 365 Q740 345 730 280" fill="none" stroke="#b5b5b5" stroke-width="2"/></svg>

<div class="service-bar left" style="top:1346px"><h3>Heat Pumps</h3><small>Sales, Installation, Servicing</small>
  <div class="service-icon light"><div class="disc"><svg width="40" height="30" viewBox="0 0 40 30"><rect x="2" y="4" width="36" height="22" fill="none" stroke="#58ab2c" stroke-width="3"/><circle cx="26" cy="15" r="6" fill="none" stroke="#58ab2c" stroke-width="3"/></svg></div></div></div>
<div class="service-bar left" style="top:1451px"><h3>Fire</h3><small>Detectors, Alarms, Wiring</small>
  <div class="service-icon"><div class="disc"><svg width="30" height="36" viewBox="0 0 30 36"><path d="M15 2C18 12 27 15 27 24a12 12 0 0 1-24 0c0-6 5-9 6-15 3 4 3 7 6 9 1-5 0-11 0-16z" fill="#fff"/></svg></div></div></div>
<div class="service-bar left" style="top:1556px"><h3>Free view TV</h3><small>Compliance</small>
  <div class="service-icon light"><div class="disc"><svg width="38" height="34" viewBox="0 0 38 34"><rect x="2" y="8" width="34" height="24" fill="none" stroke="#58ab2c" stroke-width="3"/><path d="M12 2l7 6 7-6" fill="none" stroke="#58ab2c" stroke-width="3"/></svg></div></div></div>
<div class="service-bar left" style="top:1661px"><h3>Solar</h3><small>Networks, Cabling</small>
  <div class="service-icon"><div class="disc"><svg width="36" height="36" viewBox="0 0 36 36"><circle cx="18" cy="18" r="15" fill="none" stroke="#fff" stroke-width="3"/><path d="M18 3v30M3 18h30" stroke="#fff" stroke-width="3"/></svg></div></div></div>

<div class="service-bar right" style="top:1346px"><h3>Electrical</h3><small>Commercial &amp; Residential</small>
  <div class="service-icon light"><div class="disc"><svg width="30" height="38" viewBox="0 0 30 38"><path d="M15 3a11 11 0 0 0-6 20v6h12v-6a11 11 0 0 0-6-20zM10 34h10" fill="none" stroke="#58ab2c" stroke-width="3"/></svg></div></div></div>
<div class="service-bar right" style="top:1451px"><h3>Data Cabling</h3><small>Maintenance, Servicing</small>
  <div class="service-icon"><div class="disc"><svg width="38" height="26" viewBox="0 0 38 26"><rect x="10" y="3" width="22" height="20" rx="3" fill="none" stroke="#fff" stroke-width="3"/><path d="M2 13h8" stroke="#fff" stroke-width="3"/></svg></div></div></div>
<div class="service-bar right" style="top:1556px"><h3>Eco Green</h3><small>Security, Residential, Industrial</small>
  <div class="service-icon light"><div class="disc"><svg width="40" height="30" viewBox="0 0 40 30"><path d="M19 27C8 27 3 18 3 6c10 0 16 6 16 21zM21 27c11 0 16-9 16-21-10 0-16 6-16 21z" fill="#58ab2c"/></svg></div></div></div>
<div class="service-bar right" style="top:1661px"><h3>Security</h3><small>Cameras, Networks</small>
  <div class="service-icon"><div class="disc"><svg width="32" height="38" viewBox="0 0 32 38"><path d="M16 2l13 5v10c0 9-6 16-13 19C9 33 3 26 3 17V7z" fill="none" stroke="#fff" stroke-width="3"/><path d="M10 19l5 5 8-9" fill="none" stroke="#fff" stroke-width="3"/></svg></div></div></div>

<div class="hub"><div class="brand-dot"></div><div class="brand-name">Kowhai<br>Group</div></div>

<section>
  <div class="section-title" style="top:1918px"><div class="mark"></div><h2>Our <em>Projects</em></h2><div class="rule"></div></div>
  <div class="project-photo side" style="left:44px;top:2121px;width:296px;height:242px;background:var(--photo-brick)" role="img" aria-label="Photo of a commercial building on a street corner"></div>
  <div class="project-photo main" style="left:340px;top:2088px;width:520px;height:308px;background:var(--photo-grey)" role="img" aria-label="Photo of the renovated bank branch building"></div>
  <div class="project-photo side" style="left:860px;top:2121px;width:296px;height:242px;background:var(--photo-shop)" role="img" aria-label="Photo of a retail shopfront on a town street"></div>
  <div class="project-caption" style="top:2420px"><h3>Harbour Bank - Re-modeling</h3><p>Harbour Bank New Building Project - Electrical work for building owner.</p></div>
  <div class="slider-dots" style="left:556px;top:2529px"><span style="background:var(--green)"></span><span style="background:#ccc"></span><span style="background:#ccc"></span><span style="background:#ccc"></span><span style="background:#ccc"></span></div>
</section>

<footer class="site-footer">
  <div class="footer-brand"><div class="brand-dot"></div><div class="brand-name">Kowhai<br>Group</div></div>
  <ul class="contact-list" style="top:270px">
    <li style="top:0"><span class="ico"><svg width="18" height="18" viewBox="0 0 18 18"><path d="M3 1l4 1 1 4-2 2a10 10 0 0 0 4 4l2-2 4 1 1 4-2 2C8 17 1 10 1 3z" fill="#fff"/></svg></span>0800 55 01 20 / (06) 555 0142</li>
    <li style="top:70px"><span class="ico"><svg width="18" height="18" viewBox="0 0 18 18"><rect x="2" y="5" width="14" height="11" fill="none" stroke="#fff" stroke-width="2"/><rect x="5" y="1" width="8" height="5" fill="#fff"/></svg></span>(06) 555 0187</li>
    <li style="top:130px"><span class="ico"><svg width="16" height="20" viewBox="0 0 16 20"><path d="M8 1a6 6 0 0 0-6 6c0 5 6 12 6 12s6-7 6-12a6 6 0 0 0-6-6z" fill="none" stroke="#fff" stroke-width="2"/><circle cx="8" cy="7" r="2" fill="#fff"/></svg></span>14 Harbour Lane, PO Box 4820<br>Wanganui, 4500</li>
  </ul>
  <form class="contact-form">
    <h3>Contact Form</h3><div class="rule"></div>
    <p class="note">Send an email. All fields with an * are required</p>
    <span class="field-label" style="top:135px">Name *</span><span class="field" style="top:128px"></span>
    <span class="field-label" style="top:181px">Email *</span><span class="field" style="top:174px"></span>
    <span class="field-label" style="top:227px">Subject *</span><span class="field" style="top:220px"></span>
    <span class="field-label" style="top:273px">Message *</span><span class="field" style="top:266px;height:96px"></span>
    <span class="btn-green" style="left:99px;top:384px;width:98px;height:39px;border:1.5px solid #fff;font-size:14px">Send Now</span>
  </form>
  <div class="hr"></div>
  <div class="copyright">Copyrights @ 2018 Kowhai Group. All Rights Reserved.</div>
  <div class="version">C20</div>
</footer>

</body>
</html>
```